Dietitian needs awesome business card

I need a contemporary design that's eye catching but professional.
My card is to given to doctors, specialists and patients alike.
I manage patients with chronic diseases
I have uploaded my logo and current business card, I would also like the other Registered Clinical Nutritionist logo incorporated into the design

Target Market(s)

Doctors, specialists and patients

Industry/Entity Type

Healthcare

Contact Information for Business Card

www.brindlecovenutrition.com.au
Ph: 0427 516 903
Fax: 6482 7315
email: marcus.k.wellfare@quorvamail.com
Space on the back of the card with: Appointment date, Appointment time and appointment location

Font styles to use
Serif

Colors
fbee3e
876aae
ffc214

Requirements
Must have
• My Logo
• Registered Clinical Nutritionist Logo
• My 4 locations - Fernhollow Medical Centre, North Kelby Health, Ashcourt Medical, Pinebrook Doctors Surgery
Nice to have
• I like the colours in my current business card

```html
<!DOCTYPE html>
<html lang="en">
<head>
<meta charset="utf-8">
<title>Brindlecove Nutrition &amp; Dietetics – Business Card</title>
<link rel="stylesheet" href="https://fonts.googleapis.com/css2?family=Roboto:wght@400;500;700&display=swap">
<style>
  :root {
    --bg: #d8d8d8;
    --card: #ffffff;
    --blue: #1a72c0;
    --blue-dark: #0f5ea8;
    --green: #8cc63f;
    --orange: #f47c20;
    --grey-text: #8a8a8a;
    --rule: #c9c9c9;
  }
  * { box-sizing: border-box; margin: 0; padding: 0; }
  html, body {
    width: 1200px; height: 1200px; overflow: hidden;
    background: var(--bg);
    font-family: "Roboto", Arial, sans-serif;
  }
  .canvas { position: relative; width: 1200px; height: 1200px; }

  .card {
    position: absolute; left: 190px; width: 820px; height: 470px;
    background: var(--card); border-radius: 40px; overflow: hidden;
    box-shadow: 0 6px 18px rgba(0,0,0,0.12);
  }
  .card--front { top: 110px; border-bottom: 12px solid var(--green); }
  .card--back { top: 620px; }

  /* brand lockup */
  .brand { position: absolute; display: flex; align-items: center; }
  .brand__dot { border-radius: 50%; background: var(--green); flex: none; }
  .brand__name { color: var(--blue); font-weight: 500; line-height: 1.05; }
  .card--front .brand { left: 130px; top: 150px; gap: 28px; }
  .card--front .brand__dot { width: 110px; height: 110px; }
  .card--front .brand__name { font-size: 50px; }
  .card--back .brand { left: 40px; top: 36px; gap: 14px; }
  .card--back .brand__dot { width: 52px; height: 52px; }
  .card--back .brand__name { font-size: 23px; }

  .appointment {
    position: absolute; left: 70px; right: 60px; bottom: 60px;
    border-bottom: 1px solid var(--rule);
    padding-bottom: 40px;
    font-size: 12px; letter-spacing: 1.5px; color: var(--grey-text);
  }

  .credential-badge {
    position: absolute; right: 44px; top: 36px;
    width: 112px; height: 54px; border-radius: 6px; background: var(--orange);
  }

  .practitioner { position: absolute; right: 44px; top: 196px; text-align: right; }
  .practitioner__name { color: var(--green); font-weight: 700; font-size: 36px; }
  .practitioner__role { color: var(--grey-text); font-size: 12px; letter-spacing: 1.4px; margin-top: 6px; }

  .contacts { position: absolute; left: 44px; top: 206px; list-style: none; }
  .contacts li {
    display: flex; align-items: center; gap: 12px;
    font-size: 13px; letter-spacing: 1.2px; color: var(--grey-text); height: 24px;
  }
  .contacts svg { width: 14px; height: 14px; flex: none; }

  .locations {
    position: absolute; left: 0; right: 0; bottom: 0; height: 150px;
    background: var(--blue); display: flex; padding: 22px 20px 0;
  }
  .location {
    flex: 1; padding: 0 16px; color: #fff; font-size: 12px;
    letter-spacing: 0.8px; line-height: 1.45;
  }
  .location + .location { border-left: 1px solid rgba(255,255,255,0.45); }
  .location__name { font-weight: 700; font-size: 13px; margin-bottom: 8px; }
</style>
</head>
<body>
<main class="canvas">

  <section class="card card--front" aria-label="Card front">
    <div class="brand">
      <span class="brand__dot"></span>
      <span class="brand__name">Brindlecove<br>Nutrition &amp; Dietetics</span>
    </div>
    <p class="appointment">Appointment date/time/location:</p>
  </section>

  <section class="card card--back" aria-label="Card back">
    <div class="brand">
      <span class="brand__dot"></span>
      <span class="brand__name">Brindlecove<br>Nutrition &amp; Dietetics</span>
    </div>

    <div class="credential-badge" role="img" aria-label="Registered Clinical Nutritionist badge"></div>

    <div class="practitioner">
      <p class="practitioner__name">Marcus Kellaway</p>
      <p class="practitioner__role">Practising Dietitian, Nutritionist, and Chef</p>
    </div>

    <ul class="contacts">
      <li>
        <svg viewBox="0 0 14 14"><rect x="3" y="1" width="8" height="12" rx="1.5" fill="none" stroke="#8cc63f" stroke-width="1.6"/></svg>
        0427 516 903
      </li>
      <li>
        <svg viewBox="0 0 14 14"><rect x="4" y="1" width="6" height="4" fill="#8cc63f"/><rect x="1" y="5" width="12" height="6" rx="1" fill="#8cc63f"/><rect x="4" y="9" width="6" height="4" fill="#fff" stroke="#8cc63f"/></svg>
        6482 7315
      </li>
      <li>
        <svg viewBox="0 0 14 14"><rect x="1" y="3" width="12" height="8" fill="none" stroke="#8cc63f" stroke-width="1.4"/><path d="M1 3 L7 8 L13 3" fill="none" stroke="#8cc63f" stroke-width="1.4"/></svg>
        marcus.k.wellfare@quorvamail.com
      </li>
      <li>
        <svg viewBox="0 0 14 14"><circle cx="7" cy="7" r="6" fill="#8cc63f"/><path d="M1 7 H13 M7 1 C4 4 4 10 7 13 M7 1 C10 4 10 10 7 13" fill="none" stroke="#fff" stroke-width="0.9"/></svg>
        www.brindlecovenutrition.com.au
      </li>
    </ul>

    <div class="locations">
      <div class="location">
        <p class="location__name">Fernhollow Medical Centre</p>
        <p>Cnr Alder &amp; Quill Streets<br>Fernhollow<br>Tasmania 7311<br>fernhollowmedical.com.au</p>
      </div>
      <div class="location">
        <p class="location__name">Ashcourt Medical</p>
        <p>4/118 Ravelin Road<br>Ashcourt<br>Tasmania 7314</p>
      </div>
      <div class="location">
        <p class="location__name">North Kelby Health</p>
        <p>7 Callow Drive<br>North Kelby<br>Tasmania 7316<br>northkelbyhealth.com.au</p>
      </div>
      <div class="location">
        <p class="location__name">Pinebrook Doctors Surgery</p>
        <p>9 Marlow Road<br>Pinebrook<br>Tasmania<br>pinebrookdoctors.com.au</p>
      </div>
    </div>
  </section>

</main>
</body>
</html>
```